Personal coach needs brochure design for inspirational essay about authenticity

Overview:
I want a beautiful brochure, 11”x17” that folds to 8-1/2”x11” with 4 pages. Think of it as an oversize greeting card.
• Front cover: photograph of a dancer and title with attribution of quote (Lumafold jpeg photo attached)
• Inside spread: Copy (Helena Brisk copy attached) with some appropriate illustration, based on cover photo
• Back cover: contact information, brief descriptive copy, two small photos (jpeg photo attached; see copy for direction)
Copy for front cover title, inside spread and back cover is attached in doc titled "Helena Brisk copy"

Purpose of brochure:
I'm a personal coach and once a year I produce a 4-page illustrated inspirational essay, which invites personal reflection on living a more mindful, meaningful life. Most people I send them to collect them. Someday in the future I'd like to put a collection of these essays into a coffee table book and also create a website for the collection, which is related to the personal coaching that I do.
I have the brochures printed hard copy. I have attached a few examples from previous years. Each has a unique design related to its theme.

Concept:
This year’s essay theme, “There will only ever be one you!” is based on a quote by Helena Brisk, a famous modern dancer. The complete quote, which appears in the copy, is about being true to one’s authentic self. The essay is not about dance, but because the author of the quote was a dancer who personified this theme of being unique to self, I have selected a photo of dance for the cover.

Design Guidance:
Front cover: One possibility is to expand the background color of the Lumafold photo so the photo seems to emerge from the background. But I am open to ideas. I think the photo is artsy enough as it is, but there may be other ways to treat it (e.g. special effects) that would also work. The title should appear somewhere. Make the attribution (--Helena Brisk) in smaller type than the title.

Inside Spread: There may be ways to borrow a design motif from the cover photo to make the inside spread more visually interesting, i.e., not just straight copy. I think it may be helpful to make the font size of the quote larger than the rest of the copy, but it has to be read in sequence. Or maybe it's printed in same size as copy, but then also repeated and displayed by itself in larger type.

Back cover: If you look at some of the other examples I’ve sent, you’ll see how the back cover is typically handled. I want a reduced version of the cover to be placed near the line that says "this is the 16th in a series.." Then, there’s a jpeg photo of Helena Brisk that should be placed next to the copy description of her.

Need extra days to review

```html
<!DOCTYPE html>
<html lang="en">
<head>
<meta charset="utf-8">
<title>There Will Only Ever Be One You! – Brochure</title>
<link rel="stylesheet" href="https://fonts.googleapis.com/css2?family=Barlow+Condensed:wght@600&family=Roboto:ital,wght@0,400;0,500;0,700;0,900;1,400&display=swap">
<style>
  :root {
    --canvas: #bdbdbd;
    --ink-dark: #161616;
    --ink-mid: #2e2e2e;
    --orange: #f7941d;
    --white: #ffffff;
    --text-light: #f2f2f2;
    --text-dark: #1a1a1a;
  }
  * { margin: 0; padding: 0; box-sizing: border-box; }
  html, body { width: 1200px; height: 2410px; overflow: hidden; background: var(--canvas); }
  body { position: relative; font-family: "Roboto", sans-serif; }

  .spread {
    position: absolute; left: 20px; width: 1160px; height: 750px; overflow: hidden;
    background: radial-gradient(ellipse at 50% 60%, var(--ink-mid) 0%, var(--ink-dark) 70%);
    box-shadow: 0 6px 16px rgba(0,0,0,.35);
  }
  .spread--outside { top: 375px; }
  .spread--inside { top: 1285px; }
  .spread__shapes { position: absolute; inset: 0; width: 1160px; height: 750px; }

  .cover-photo {
    position: absolute; left: 580px; top: 0; width: 580px; height: 750px;
    background: radial-gradient(ellipse at 52% 58%, #4a4d55 0%, #2a2b2f 38%, #131313 80%);
  }

  .abs { position: absolute; }

  .series-intro { left: 30px; top: 116px; width: 490px; color: var(--white); font-size: 14px; line-height: 17px; }
  .address { left: 27px; top: 170px; color: var(--text-light); font-size: 14.5px; line-height: 17.5px; }
  .contact { left: 27px; color: var(--text-light); font-size: 14.5px; line-height: 22px; display: flex; align-items: center; gap: 10px; }
  .contact--phone { top: 256px; }
  .contact--mail { top: 284px; }
  .contact__icon { width: 22px; height: 22px; flex: none; }

  .about-box { left: 0; top: 334px; width: 580px; height: 219px; background: var(--white); }
  .portrait {
    position: absolute; left: 27px; top: 22px; width: 175px; height: 174px;
    border: 2px solid var(--orange);
    background: linear-gradient(150deg, #3c3c3c 0%, #1d1d1d 55%, #6a6a66 100%);
  }
  .about-heading { position: absolute; left: 233px; top: 32px; color: var(--orange); font-size: 16px; font-weight: 500; }
  .about-copy {
    position: absolute; left: 233px; top: 62px; width: 322px; color: var(--text-dark);
    font-size: 8.6px; line-height: 11px; text-align: justify;
  }
  .photo-credit { left: 43px; top: 562px; color: #cfcfcf; font-size: 8px; font-style: italic; line-height: 10px; }
  .photographer-heading { left: 27px; top: 602px; color: var(--orange); font-size: 16px; font-weight: 500; }
  .photographer-copy { left: 27px; top: 634px; width: 528px; color: var(--text-light); font-size: 8.6px; line-height: 11px; text-align: justify; }

  .cover-title {
    left: 580px; top: 58px; width: 580px; text-align: center; color: var(--white);
    font-family: "Barlow Condensed", sans-serif; font-weight: 600; font-size: 50px; line-height: 52px; letter-spacing: .5px;
  }
  .cover-attribution { left: 580px; top: 170px; width: 580px; text-align: center; color: var(--orange); font-size: 19px; }

  .essay {
    left: 54px; top: 146px; width: 478px; color: var(--text-light);
    font-size: 12.3px; line-height: 14.8px; text-align: justify;
  }
  .essay p { margin-bottom: 14px; }
  .highlight { color: var(--orange); font-weight: 500; }

  .pull-quote {
    left: 668px; top: 152px; width: 432px; text-align: center; color: var(--text-dark);
    font-size: 14.5px; line-height: 18.6px; font-weight: 500;
  }
  .reflection {
    left: 625px; top: 452px; width: 498px; color: var(--text-light);
    font-size: 12.3px; line-height: 14.8px; text-align: justify;
  }
  .reflection p { margin-bottom: 12px; }
</style>
</head>
<body>

<section class="spread spread--outside" aria-label="Outside spread: back cover and front cover">
  <div class="cover-photo" role="img" aria-label="Photograph of a leaping modern dancer in a flowing dark dress against a smoky dark backdrop"></div>

  <svg class="spread__shapes" viewBox="0 0 1160 750" aria-hidden="true">
    <polygon points="0,0 580,0 580,4 0,80" fill="var(--orange)"/>
    <line x1="0" y1="92" x2="580" y2="12" stroke="var(--white)" stroke-width="2"/>
    <polygon points="580,750 1160,750 1160,672 580,742" fill="var(--orange)"/>
    <line x1="580" y1="732" x2="1160" y2="660" stroke="var(--white)" stroke-width="2"/>
  </svg>

  <p class="abs series-intro">There Will Only Ever Be One You is the 16th in a series of Labor Day essays inviting a moment of reflection on living a more meaningful, more mindful life</p>
  <p class="abs address">Nora Valecki Hale, Ph.D.<br>Heron Ridge House<br>12 Orchard Lane<br>Millbrook, Vermont&nbsp; 05061</p>
  <p class="abs contact contact--phone">
    <svg class="contact__icon" viewBox="0 0 22 22" aria-hidden="true"><circle cx="11" cy="11" r="11" fill="var(--orange)"/><path d="M7.5 5.5l2 .3 1 2.6-1.3 1.1a7 7 0 0 0 3.3 3.3l1.1-1.3 2.6 1 .3 2c-.4 1-1.5 1.6-2.6 1.3A10 10 0 0 1 6.2 8.1c-.3-1.1.3-2.2 1.3-2.6z" fill="var(--white)"/></svg>
    555-014-2290
  </p>
  <p class="abs contact contact--mail">
    <svg class="contact__icon" viewBox="0 0 22 22" aria-hidden="true"><circle cx="11" cy="11" r="11" fill="var(--orange)"/><rect x="5.5" y="7" width="11" height="8" rx="1" fill="var(--white)"/><path d="M5.8 7.5l5.2 4 5.2-4" fill="none" stroke="var(--orange)" stroke-width="1.2"/></svg>
    nvhale@mailbox.example
  </p>

  <div class="abs about-box">
    <div class="portrait" role="img" aria-label="Black and white photograph of a dancer in a sweeping white skirt, arm raised"></div>
    <h2 class="about-heading">About Helena Brisk:</h2>
    <p class="about-copy">Born in 1894, Helena Brisk danced and taught for over 70 years.She is recognized as a primal artistic force of the 20th century, whose influence on modernity has been compared to Marco Ruel, Owen Farrel, Ilya Varsky, and Henry Lake Ashford. Her themes dealt with the lives and conflicts of ordinary people, and she brought serious issues to the stage like war, poverty, intolerance and the injustices of slavery and treatment of Native Americans. Rebelling against conventions of the past, her dancing and choreography exposed the depths of human emotion through intense movements that were forceful, stark, angular, jagged, and percussive – startlingly unlike the formality of classical ballet, which she saw as antiquated.</p>
  </div>

  <p class="abs photo-credit">"Helena Brisk in Letter to the Sky, No.<br>&nbsp;&nbsp;&nbsp;&nbsp;&nbsp;&nbsp;1"© The Clara Wendt Archive</p>
  <h2 class="abs photographer-heading">About Photographer Clara Wendt:</h2>
  <p class="abs photographer-copy">In 1935 Clara Wendt saw a performance by modern dancer and choreographer Helena Brisk. Wendt was so inspired by the dance performance that she introduced herself to Brisk, and the two artists began an artistic collaboration that lasted more than 60 years.Wendt often photographed dancers in action, to capture the emotion behind their movement. Her artistic style was in line with Brisk's philosophy of dance. This photo from the dance, "Letter to the Sky," is one of Wendt's most famous photographs. The title of this work comes from an Eliza Thorn poem, which inspired Brisk to create a dance performance based on Thorn's life.</p>

  <h1 class="abs cover-title">“THERE WILL ONLY EVER<br>BE ONE YOU!”</h1>
  <p class="abs cover-attribution">Helena&nbsp; Brisk</p>
</section>

<section class="spread spread--inside" aria-label="Inside spread: essay and quote">
  <svg class="spread__shapes" viewBox="0 0 1160 750" aria-hidden="true">
    <polygon points="0,0 1160,0 1160,88 580,58 0,88" fill="var(--white)"/>
    <polyline points="0,97 580,67 1160,97" fill="none" stroke="var(--white)" stroke-width="2"/>
    <polygon points="0,750 0,722 580,660 1160,722 1160,750" fill="var(--orange)"/>
    <polyline points="0,710 580,648 1160,710" fill="none" stroke="var(--white)" stroke-width="2"/>

    <line x1="803" y1="116" x2="1000" y2="116" stroke="var(--white)" stroke-width="3" stroke-linecap="round"/>
    <line x1="858" y1="384" x2="1028" y2="384" stroke="var(--white)" stroke-width="3" stroke-linecap="round"/>
    <path d="M626 226 Q618 284 628 342" fill="none" stroke="var(--white)" stroke-width="3" stroke-linecap="round"/>
    <path d="M1142 152 Q1150 210 1138 268" fill="none" stroke="var(--white)" stroke-width="3" stroke-linecap="round"/>

    <path d="M668,128 H1097 Q1125,128 1125,156 V337 Q1125,365 1097,365 H745 L704,410 L708,365 H668 Q640,365 640,337 V156 Q640,128 668,128 Z"
          fill="var(--white)" stroke="var(--orange)" stroke-width="2.5"/>
    <text x="643" y="218" font-family="Roboto, sans-serif" font-weight="900" font-size="112" fill="var(--orange)">“</text>
    <text x="1050" y="436" font-family="Roboto, sans-serif" font-weight="900" font-size="112" fill="var(--orange)">”</text>
  </svg>

  <div class="abs essay">
    <p>In the rural Ohio village where I grew up, one of the highlights of Sunday morning church service -- in between congregational hymn-singing and the preacher's sermon -- was the "special selection," a musical performance by a parishioner. Typically, it was a vocalist or instrumental on piano, organ or violin. One Sunday, we were surprised by an unusual performance. A plump, buxom farm wife approached the pulpit, puckered up her lips and unexpectedly began to whistle the hymn "The Quiet Hill." As a 10-year-old, I found this hilarious as I tried to choke back my wide-eyed amazement and giggles.</p>
    <p>Despite the irreverence of my pre-adolescent reaction, this memory has stayed with me for decades as an iconic example of the wonderment of individual differences. Of the delight I find in witnessing someone express herself in sometimes surprising and even courageous ways. Of the marvel of beholding a person be truly authentic and uniquely original.</p>
    <p>Someone who personified the irrepressible impulse to express her individuality was the early 20th century dancer and choreographer Helena Brisk. A pioneer of modern dance, she threw tradition overboard and was inspired to dance in a way that was radical departure from the formalized style and rigidly dictated forms of classical ballet. Brisk felt compelled to express the rawness and emotion of human experience in her dancing -- not just present a form of pretty entertainment. Iconoclastically brilliant, she created a new language of dance, a revolutionary vocabulary of movement that electrified the stage, often creating a visceral response in the audience.</p>
    <p>In her biography of Brisk, her friend and equally talented choreographer Ada Marlow recalled that despite sensational reviews for her own innovative work in the Broadway musical Prairie Song!, Marlow had a gnawing feeling that her work was only mediocre. Marlow confessed her anxieties to Brisk who listened quietly and then responded, <span class="highlight">"There will only ever be one you!"</span> Continuing, she added:</p>
  </div>

  <p class="abs pull-quote">There is a vitality, a life-force, an energy, a quickening that is translated through you into action. And because there is only one of you in all of time, this expression is unique. And if you block it, the world will not have it. It is not your business to determine how good it is nor how valuable nor how it compares with other expressions. It is your business to keep it yours clearly and directly, to keep the channel open. You have to keep open and aware directly to the urges that motivate you. Above all else, keep the channel open!"</p>

  <div class="abs reflection">
    <p>Brisk's wisdom reminds us that we must not hold back or judge our gifts. Although there may be moments when we doubt ourselves or when we worry that we're not good enough, our job is to be fearless and to <span class="highlight">"keep the channel open."</span></p>
    <p>Guard the precious miracle of your own uniqueness.Find that home-sweet- home feeling where you feel you are your most authentic self. There will only ever be one you! And importantly, respect the differences of others. Our world would be a drab, boring place if we all only whistled one tune.</p>
  </div>
</section>

</body>
</html>
```